A.I. Software PowerPoint Presentation

We need a PowerPoint presentation design for our artificial intelligence product vxMender.

We've attached our current PowerPoint to use as a base. This presentation is used to introduce and describe what the product is, how it works, why you need it, what makes it better than other solutions, and how to implement it.

We would like the PowerPoint design to be more professional-looking as we present to executives and CIOs of banks, government, and other large corporations. We are a tech startup and would like the design to convey the feel of innovation and high-tech, but also trustworthy, reputable, and capable, for the more conservative audiences.

The PowerPoint should have minimal use of animation (animate only if necessary). It should be modern and clean and not too busy.

We appreciate design work on all of the following: slide backgrounds, title slide, fonts, pictures used in the slides, layout, charts, graphics, comparison versus, etc. If you have any ideas for the slide contents, please also provide any suggestions/recommendations.

I've also attached our vxMender logo if that is needed, as well as our brochure.

We look forward to your submissions!

EDIT:
I would like to add that we are using PowerPoint 2010 on a PC (.pptx file), and that the slides should be in 16:9 mainly but also with 4:3 version (if possible cut off the sides and squish in the content a little, no need to make a new set of slides) as sometimes we cannot control whose projector we are presenting on. Thanks

Target Market(s)

Enterprise clients, multi-national corporations,
banks, airlines, telecommunications, government

Industry/Entity Type

Software

Font styles to use
Serif
Sans Serif

Colors

Designer to choose colors to be used in the design.

Requirements
Nice to have
• Professional, clean-look, modern design
Should not have
• Should not look cheesy (i.e. tons of stock photos, business cliche pictures)
• Should not look over-done/over-the-top
• Should not look outdated

```html
<!DOCTYPE html>
<html lang="en">
<head>
<meta charset="utf-8">
<title>vxMender – Enterprise Chatbot Platform</title>
<link href="https://fonts.googleapis.com/css2?family=Open+Sans:wght@400;600;700&family=Montserrat:wght@700&display=swap" rel="stylesheet">
<style>
:root{
  --navy:#1565c0;
  --sky:#3aa8e8;
  --sky-pale:#e6f3fc;
  --grey:#a7a7a7;
  --ink:#555;
  --orange:#f7941d;
  --page:#ece8e1;
  --white:#fff;
}
*{box-sizing:border-box;margin:0;padding:0}
html,body{width:1200px;height:2161px;overflow:hidden;background:var(--page);font-family:"Open Sans",Arial,sans-serif;color:var(--ink)}
.board{position:relative;width:1200px;height:2161px}
.slide{position:absolute;width:537px;height:303px;background:var(--white);box-shadow:0 2px 6px rgba(0,0,0,.18);overflow:hidden}
.col-l{left:52px}.col-r{left:624px}
.r1{top:341px}.r2{top:684px}.r3{top:1027px}.r4{top:1370px}.r5{top:1713px}
.abs{position:absolute}
.slide-title{position:absolute;left:27px;top:18px;font-family:"Montserrat","Open Sans",sans-serif;font-size:19px;color:var(--navy);letter-spacing:.3px}
.slide-sub{position:absolute;left:27px;top:54px;font-size:8px;color:var(--ink)}
.foot-logo{position:absolute;left:24px;bottom:10px;display:flex;align-items:center;gap:4px;font-size:11px;color:var(--sky);font-weight:600}
.foot-logo i,.brand i{display:inline-block;border-radius:50%;background:var(--sky)}
.foot-logo i{width:10px;height:10px}
.page-no{position:absolute;right:24px;bottom:12px;font-size:7px;color:var(--navy)}
/* title */
.title-slide{left:336px;top:14px;height:303px}
.title-slide .brand{position:absolute;left:300px;top:115px;display:flex;align-items:center;gap:10px;font-size:34px;color:var(--sky);font-weight:600}
.brand i{width:30px;height:30px;background:var(--navy)}
.title-band{position:absolute;left:0;top:190px;width:100%;height:29px;background:var(--navy);color:#fff;font-weight:700;font-size:17px;padding:3px 28px}
.title-lower{position:absolute;left:0;top:219px;width:100%;height:84px;background:var(--sky);color:#fff;font-size:11px;padding:14px 28px}
.title-lower small{position:absolute;right:24px;bottom:10px;font-size:6px;opacity:.8}
/* cards */
.card{position:absolute;top:91px;width:121px;height:158px;border:2px solid var(--navy);background:#fff}
.card .head{height:68px;background:var(--navy);color:#fff;font-size:9.5px;font-weight:600;text-align:center;display:flex;align-items:center;justify-content:center;padding:4px 8px;line-height:1.25}
.card.light{border-color:var(--sky)}.card.light .head{background:var(--sky)}
.card .body{height:86px;display:flex;align-items:center;justify-content:center;flex-wrap:wrap;gap:6px;padding:8px}
.badge{width:42px;height:22px;border-radius:4px;background:#d9dee6}
.badge.round{width:30px;height:30px;border-radius:50%}
/* chart */
.chart-box{position:absolute;left:23px;top:79px;width:484px;height:176px;border:2px solid var(--navy)}
/* tiles */
.tile-label{position:absolute;width:105px;text-align:center;font-size:13px;font-weight:600}
.tile{position:absolute;top:141px;width:104px;height:68px;display:flex;align-items:center;justify-content:center}
.dark{background:var(--navy);color:var(--navy)}.lite{background:var(--sky);color:var(--sky)}
/* intro */
.tagline{position:absolute;left:42px;top:90px;font-size:11px;font-weight:600;color:var(--sky)}
.logo-frame{position:absolute;left:42px;top:111px;width:289px;height:119px;border:2px solid var(--navy);display:flex;align-items:center;justify-content:center;gap:12px;font-size:36px;color:var(--sky);font-weight:600}
.logo-frame i{width:40px;height:40px;border-radius:50%;background:var(--navy)}
.pill{position:absolute;left:337px;width:120px;height:33px;background:var(--navy);color:#fff;font-size:9px;display:flex;align-items:center;gap:8px;padding:0 8px;line-height:1.1}
/* screenshot */
.shot{position:absolute;left:56px;top:53px;width:380px;height:213px;background:linear-gradient(180deg,#f3f4f6,#dfe2e6);border:1px solid #ccc}
.shot-chat{position:absolute;left:213px;top:56px;width:138px;height:223px;background:linear-gradient(180deg,#eef2ef,#d5d8d6);border:2px solid #9fb3a8;border-radius:4px}
/* features */
.feat{position:absolute;display:flex;align-items:center;gap:8px;font-size:9.5px;line-height:1.2;width:200px}
.feat .ic{width:56px;height:39px;flex:none;display:flex;align-items:center;justify-content:center}
.feat.lt{color:var(--sky)}.feat.dk{color:var(--navy)}
.ic.lt{background:var(--sky)}.ic.dk{background:var(--navy)}
/* comparison */
.cmp{position:absolute;top:95px;width:149px;height:169px;font-size:8px;line-height:1.25}
.cmp.old{left:69px;border:2px solid var(--grey)}
.cmp.new{left:308px;border:2px solid var(--sky)}
.cmp .h{height:40px;display:flex;align-items:center;justify-content:center;color:#fff;font-weight:700;font-size:10px;gap:5px}
.cmp.old .h{background:var(--grey)}.cmp.new .h{background:var(--sky)}
.cmp.new .h i{width:11px;height:11px;border-radius:50%;background:#fff;display:inline-block}
.cmp ul{list-style:none;padding:10px 10px 0 14px}
.cmp li{position:relative;padding-left:9px;margin-bottom:9px}
.cmp li:before{content:"";position:absolute;left:0;top:4px;width:3px;height:3px;border-radius:50%;background:currentColor}
.cmp.new li{color:var(--navy)}
.cmp.new li:before{background:var(--sky)}
.cmp .grp{padding:10px 0 0 10px;font-weight:600;color:var(--ink)}
.cmp .grp + ul{padding-top:4px}
.vs{position:absolute;left:258px;top:180px;font-size:12px;font-weight:700;color:var(--sky)}
.corner-ic{position:absolute;left:439px;top:17px;width:59px;height:38px;background:var(--navy);display:flex;align-items:center;justify-content:center}
/* steps */
.step{position:absolute;top:91px;width:128px;height:167px;border:2px solid var(--sky);text-align:center;font-size:8px;line-height:1.5}
.step .ph{height:103px;background:linear-gradient(180deg,#d7d9dc,#9ea3a8)}
.step .num{position:absolute;right:-2px;top:88px;width:30px;height:28px;background:var(--sky);color:#fff;font-size:16px;font-weight:700;display:flex;align-items:center;justify-content:center}
.step p{padding-top:22px}
.step b{color:var(--navy);font-weight:600}
.mode{position:absolute;top:264px;width:114px;height:15px;background:var(--orange);color:#fff;font-size:7.5px;text-align:center;line-height:15px}
/* media */
.media{position:absolute;width:157px;height:66px;border:2px solid var(--sky)}
.media-cap{position:absolute;width:157px;text-align:center;font-size:7.5px;color:var(--sky);line-height:1.15}
</style>
</head>
<body>
<main class="board">

  <section class="slide title-slide">
    <div class="brand"><i></i>vxMender</div>
    <div class="title-band">Enterprise Chatbot Platform</div>
    <div class="title-lower">April 22, 2017<small>vxMender © 2017</small></div>
  </section>

  <!-- 2 -->
  <section class="slide col-l r1">
    <h2 class="slide-title">CONTEXT</h2>
    <p class="slide-sub">We've spent the last ~25 years building end-to-end automation solutions for leading companies</p>
    <div class="card" style="left:62px"><div class="head">A track record of long term relationships with top companies</div>
      <div class="body"><span class="badge"></span><span class="badge"></span><span class="badge round"></span></div></div>
    <div class="card light" style="left:209px"><div class="head">Experts in custom automation + business intelligence systems</div>
      <div class="body"><svg width="52" height="52" viewBox="0 0 52 52"><circle cx="26" cy="26" r="22" fill="var(--sky)"/><circle cx="20" cy="22" r="3" fill="#fff"/><circle cx="32" cy="20" r="3" fill="#fff"/><circle cx="27" cy="32" r="3" fill="#fff"/><path d="M20 22L32 20L27 32Z" fill="none" stroke="#fff" stroke-width="1.5"/></svg></div></div>
    <div class="card" style="left:353px"><div class="head">Toronto – based, but with a growing global footprint</div>
      <div class="body"><svg width="52" height="52" viewBox="0 0 52 52" fill="none" stroke="var(--navy)" stroke-width="3"><circle cx="26" cy="22" r="15"/><path d="M11 22h30M26 7c-8 8-8 22 0 30M26 7c8 8 8 22 0 30"/><path d="M6 30c4 12 14 16 20 16s16-4 20-16" stroke-linecap="round"/></svg></div></div>
    <div class="foot-logo"><i></i>vxMender</div><span class="page-no">2</span>
  </section>

  <!-- 3 -->
  <section class="slide col-r r1">
    <h2 class="slide-title">CONTEXT</h2>
    <p class="slide-sub">...And because of technology, the way these companies interact with their customers is about to change!</p>
    <div class="chart-box">
      <svg width="480" height="172" viewBox="0 0 480 172" font-family="Open Sans, sans-serif">
        <text x="26" y="75" font-size="9" fill="#333" transform="rotate(-90 26 75)" text-anchor="middle">Maturity</text>
        <line x1="44" y1="12" x2="44" y2="142" stroke="#333"/><line x1="44" y1="142" x2="280" y2="142" stroke="#333"/>
        <path d="M58 140 C150 138 230 120 275 70" fill="none" stroke="#f5c518" stroke-width="4"/>
        <path d="M58 140 C150 136 225 110 276 50" fill="none" stroke="var(--sky)" stroke-width="4"/>
        <path d="M58 140 C150 134 222 100 276 28" fill="none" stroke="var(--navy)" stroke-width="4"/>
        <path d="M270 62l9-6-2 11z" fill="#f5c518"/><path d="M270 44l9-6-2 11z" fill="var(--sky)"/><path d="M270 22l9-6-2 11z" fill="var(--navy)"/>
        <g font-size="9" fill="#333"><text x="60" y="158">80s</text><text x="110" y="158">90s</text><text x="160" y="158">00s</text><text x="210" y="158">10s</text><text x="260" y="158">20s</text><text x="300" y="153">Year</text></g>
        <g font-size="7.5" fill="#333">
          <path d="M312 77h8l-3-3M320 77l-3 3" stroke="var(--navy)" stroke-width="2" fill="none"/><text x="326" y="80">Artificial Intelligence</text>
          <path d="M312 95h8l-3-3M320 95l-3 3" stroke="var(--sky)" stroke-width="2" fill="none"/><text x="326" y="98">Machine Learning</text>
          <path d="M312 113h8l-3-3M320 113l-3 3" stroke="#f5c518" stroke-width="2" fill="none"/><text x="326" y="116">Natural Language Processing</text>
        </g>
      </svg>
    </div>
    <div class="foot-logo"><i></i>vxMender</div><span class="page-no">3</span>
  </section>

  <!-- 4 -->
  <section class="slide col-l r2">
    <h2 class="slide-title">CONTEXT</h2>
    <p class="slide-sub">Digital customer experience is becoming the new battleground (for winning customer hearts and wallets)</p>
    <span class="tile-label" style="left:70px;top:113px;color:var(--navy)">On-demand</span>
    <span class="tile-label" style="left:215px;top:113px;color:var(--sky)">Low Friction</span>
    <span class="tile-label" style="left:361px;top:113px;color:var(--navy)">Intuitive</span>
    <div class="tile dark" style="left:71px"><svg width="42" height="30" viewBox="0 0 42 30" fill="none" stroke="#fff" stroke-width="3"><path d="M4 4l16 11-16 11zM20 4l16 11-16 11z"/></svg></div>
    <div class="tile lite" style="left:216px"><svg width="40" height="36" viewBox="0 0 40 36" fill="none" stroke="#fff" stroke-width="3" stroke-linecap="round"><path d="M6 12h22l-5-5M34 24H12l5 5"/></svg></div>
    <div class="tile dark" style="left:362px"><svg width="36" height="40" viewBox="0 0 36 40" fill="none" stroke="#fff" stroke-width="2.5" stroke-linecap="round"><path d="M16 14v16l-4-4M16 18l10 2v10c0 4-3 7-7 7h-3"/><path d="M16 3v4M8 7l3 3M24 7l-3 3M6 14h3M23 14h3"/></svg></div>
    <div class="foot-logo"><i></i>vxMender</div><span class="page-no">4</span>
  </section>

  <!-- 5 -->
  <section class="slide col-r r2">
    <h2 class="slide-title">INTRODUCING VXMENDER</h2>
    <p class="slide-sub">And achieving customer experience success has just become a lot easier – Introducing vxMender!</p>
    <span class="tagline">A Cutting-Edge Enterprise Chatbot Platform:</span>
    <div class="logo-frame"><i></i>vxMender</div>
    <div class="pill" style="top:157px"><svg width="16" height="14" viewBox="0 0 16 14" fill="#fff"><rect x="1" y="8" width="3" height="6"/><rect x="6" y="5" width="3" height="9"/><rect x="11" y="2" width="3" height="12"/></svg>Customer<br>Experience</div>
    <div class="pill" style="top:196px"><svg width="16" height="14" viewBox="0 0 16 14" fill="#fff"><rect x="1" y="2" width="3" height="12"/><rect x="6" y="6" width="3" height="8"/><rect x="11" y="9" width="3" height="5"/></svg>Cost</div>
    <div class="foot-logo"><i></i>vxMender</div><span class="page-no">5</span>
  </section>

  <!-- 6 -->
  <section class="slide col-l r3">
    <h2 class="slide-title">INTRODUCING VXMENDER <span style="font-family:'Open Sans',sans-serif;font-size:8px;color:var(--ink);font-weight:400;letter-spacing:0">And vxMender is really, really easy to use for customers</span></h2>
    <div class="shot" role="img" aria-label="Screenshot of a services website in a browser"></div>
    <div class="shot-chat" role="img" aria-label="Screenshot of the vxMender chat window open on the website"></div>
    <div class="foot-logo"><i></i>vxMender</div><span class="page-no">6</span>
  </section>

  <!-- 7 -->
  <section class="slide col-r r3">
    <h2 class="slide-title">INTRODUCING VXMENDER</h2>
    <p class="slide-sub">Digital customer experience is becoming the new battleground (for winning customer hearts and wallets)</p>
    <div class="feat lt" style="left:84px;top:91px"><span class="ic lt"><svg width="22" height="22" viewBox="0 0 22 22" fill="none" stroke="#fff" stroke-width="2"><circle cx="11" cy="11" r="9"/><path d="M2 11h18M11 2c-4 4-4 14 0 18M11 2c4 4 4 14 0 18"/></svg></span>Omni-Language<br>Performance</div>
    <div class="feat dk" style="left:84px;top:151px"><span class="ic dk"><svg width="20" height="24" viewBox="0 0 20 24" fill="none" stroke="#fff" stroke-width="2"><rect x="2" y="2" width="16" height="20" rx="2"/><path d="M6 8h8M6 12h8M6 16h5"/></svg></span>Real World<br>Natural Language<br>Interaction</div>
    <div class="feat lt" style="left:84px;top:212px"><span class="ic lt"><svg width="22" height="20" viewBox="0 0 22 20" fill="none" stroke="#fff" stroke-width="2"><path d="M2 7h4l5-4v14l-5-4H2z" fill="#fff"/><path d="M15 6c2 2 2 6 0 8M18 3c4 4 4 10 0 14"/></svg></span>Mixed-Media<br>Responses</div>
    <div class="feat dk" style="left:287px;top:91px"><span class="ic dk"><svg width="22" height="22" viewBox="0 0 22 22" fill="#fff"><path d="M20 2c-7 0-12 4-14 10l4 4c6-2 10-7 10-14zM5 13l-3 7 7-3z"/></svg></span>Fast Impact</div>
    <div class="feat lt" style="left:287px;top:151px"><span class="ic lt"><svg width="20" height="22" viewBox="0 0 20 22" fill="#fff"><path d="M10 1l8 3v6c0 6-4 10-8 11-4-1-8-5-8-11V4z"/></svg></span>Keeps your data<br>secure</div>
    <div class="feat dk" style="left:287px;top:212px"><span class="ic dk"><svg width="24" height="22" viewBox="0 0 24 22" fill="none" stroke="#fff" stroke-width="3"><circle cx="9" cy="12" r="5"/><circle cx="18" cy="6" r="3"/></svg></span>Low Cost<br>Independent<br>Operations</div>
    <div class="foot-logo"><i></i>vxMender</div><span class="page-no">7</span>
  </section>

  <!-- 8 -->
  <section class="slide col-l r4">
    <h2 class="slide-title">INTRODUCING VXMENDER</h2>
    <p class="slide-sub">Omni-Language Performance</p>
    <div class="corner-ic"><svg width="24" height="24" viewBox="0 0 22 22" fill="none" stroke="#fff" stroke-width="2"><circle cx="11" cy="11" r="9"/><path d="M2 11h18M11 2c-4 4-4 14 0 18M11 2c4 4 4 14 0 18"/></svg></div>
    <div class="cmp old"><div class="h">Traditional AI/NLP</div>
      <ul style="padding-top:60px"><li>Language dependent: only 1 language at a time</li><li>Rule-based</li><li>Multiple layers of translation</li></ul></div>
    <span class="vs">vs.</span>
    <div class="cmp new"><div class="h"><i></i>vxMender</div>
      <p class="grp">Language independent</p>
      <ul><li>Supports all known written/spoken languages</li><li>Supports mixed-language dialogs</li></ul>
      <p class="grp" style="padding-top:0">Statistics-based</p>
      <ul><li>No translation layers</li></ul></div>
    <div class="foot-logo"><i></i>vxMender</div><span class="page-no">8</span>
  </section>

  <!-- 9 -->
  <section class="slide col-r r4">
    <h2 class="slide-title">INTRODUCING VXMENDER</h2>
    <p class="slide-sub">Real World Natural Language Interaction</p>
    <div class="corner-ic"><svg width="20" height="24" viewBox="0 0 20 24" fill="none" stroke="#fff" stroke-width="2"><rect x="2" y="2" width="16" height="20" rx="2"/><path d="M6 8h8M6 12h8M6 16h5"/></svg></div>
    <div class="cmp old"><div class="h">Traditional AI/NLP</div>
      <ul style="padding-top:30px"><li>Voice commands</li><li>Keyword matching</li><li style="margin-top:30px">Programmed in isolation</li></ul></div>
    <span class="vs">vs.</span>
    <div class="cmp new"><div class="h"><i></i>vxMender</div>
      <ul style="padding-top:30px"><li>True NLP</li><li style="margin-top:36px">Trained on-the-job from real conversations</li></ul></div>
    <div class="foot-logo"><i></i>vxMender</div><span class="page-no">9</span>
  </section>

  <!-- 10 -->
  <section class="slide col-l r5">
    <h2 class="slide-title">INTRODUCING VXMENDER</h2>
    <p class="slide-sub">Real World Natural Language Interaction</p>
    <div class="corner-ic"><svg width="20" height="24" viewBox="0 0 20 24" fill="none" stroke="#fff" stroke-width="2"><rect x="2" y="2" width="16" height="20" rx="2"/><path d="M6 8h8M6 12h8M6 16h5"/></svg></div>
    <div class="step" style="left:72px"><div class="ph" role="img" aria-label="Photo of a live agent working at a laptop"></div><span class="num">1</span><p>Live agent works<br><b>vxMender learns</b></p></div>
    <div class="step" style="left:212px;width:116px"><div class="ph" role="img" aria-label="Photo of a live agent beside a robot"></div><span class="num">2</span><p>vxMender works<br><b>Live agent verifies</b></p></div>
    <div class="step" style="left:351px;width:114px"><div class="ph" role="img" aria-label="Photo of a robot working at a laptop"></div><span class="num">3</span><p><b>vxMender works<br>independently</b></p></div>
    <div class="mode" style="left:213px">Semi-automatic Mode</div>
    <div class="mode" style="left:351px">Automatic Mode</div>
    <div class="foot-logo"><i></i>vxMender</div><span class="page-no">10</span>
  </section>

  <!-- 11 -->
  <section class="slide col-r r5">
    <h2 class="slide-title">INTRODUCING VXMENDER</h2>
    <p class="slide-sub">Mixed-Media Response Modules</p>
    <div class="corner-ic"><svg width="22" height="20" viewBox="0 0 22 20" fill="none" stroke="#fff" stroke-width="2"><path d="M2 7h4l5-4v14l-5-4H2z" fill="#fff"/><path d="M15 6c2 2 2 6 0 8M18 3c4 4 4 10 0 14"/></svg></div>
    <div class="media" style="left:23px;top:82px;background:linear-gradient(135deg,#6fa3d8,#1f4f8a)" role="img" aria-label="Image of a globe with media"></div>
    <div class="media" style="left:190px;top:82px;background:linear-gradient(135deg,#f4f4f4,#8a8a8a)" role="img" aria-label="Photo of a magnifying glass"></div>
    <div class="media" style="left:359px;top:82px;background:#f2f2f2;display:flex;flex-direction:column;align-items:center;justify-content:center;font-size:8px;color:#333"><b style="font-size:9px">Error</b>You entered an incorrect password</div>
    <div class="media" style="left:23px;top:176px;background:linear-gradient(135deg,#f1f1f1,#a9a9a9)" role="img" aria-label="Photo of a ticket form being filled"></div>
    <div class="media" style="left:190px;top:176px;background:linear-gradient(135deg,#efefef,#b3b3b3)" role="img" aria-label="Photo of a hand writing on a survey"></div>
    <div class="media" style="left:359px;top:176px;background:linear-gradient(135deg,#e9edf0,#8e9aa3)" role="img" aria-label="Photo of a pen filling a form"></div>
    <span class="media-cap" style="left:23px;top:150px">Media Responses<br><span style="color:var(--ink);font-size:6px">(e.g. video and sound)</span></span>
    <span class="media-cap" style="left:190px;top:150px">Account Info Lookup</span>
    <span class="media-cap" style="left:359px;top:150px">Password Reset</span>
    <span class="media-cap" style="left:23px;top:244px">Email or Ticket Creation</span>
    <span class="media-cap" style="left:190px;top:244px">User Feedback Surveys</span>
    <span class="media-cap" style="left:359px;top:244px">Form Filling</span>
    <div class="foot-logo"><i></i>vxMender</div><span class="page-no">11</span>
  </section>

</main>
</body>
</html>
```